Web Design for Financial Consulting Company

We need a website design for a financial consulting company "Kelvane Consulting". We build financial models, scenario analysis, handle the budgeting process and provide temporary staffing. I have over 10 years of experience. My Excel expertise and analytical savvy has saved clients over $17 million in profit.

Target Market(s)

Small to medium businesses

Industry/Entity Type

Financial Consulting

Number of Pages Required

4 page

Requirements
Must have
• Professional looking
Nice to have
• A little futuristic looking

```html
<!DOCTYPE html>
<html lang="en">
<head>
<meta charset="utf-8">
<title>Kelvane Consulting</title>
<link href="https://fonts.googleapis.com/css2?family=Roboto:wght@400;500;700&display=swap" rel="stylesheet">
<style>
:root{
  --navy:#0c3a66;
  --navy-deep:#0a1a3c;
  --blue:#00a8ef;
  --ink:#18222f;
  --footer:#16212e;
  --field:#f1f1f1;
  --field-line:#d4d4d4;
  --white:#ffffff;
}
*{margin:0;padding:0;box-sizing:border-box}
html,body{width:1200px;height:4057px;overflow:hidden}
body{position:relative;background:var(--white);font-family:'Roboto',Arial,sans-serif;color:var(--ink)}
.abs{position:absolute}
.brand{display:flex;align-items:center;gap:10px;font-weight:700;font-size:20px;letter-spacing:1px;color:var(--navy)}
.brand-mark{width:26px;height:26px;background:var(--blue)}
.site-header{top:0;left:0;width:1200px;height:126px}
.site-header .brand{position:absolute;left:60px;top:48px}
.nav{position:absolute;top:54px;font-size:14px;font-weight:500;color:var(--navy)}
.btn{position:absolute;display:flex;align-items:center;justify-content:center;background:var(--blue);color:var(--white);font-size:13px;font-weight:700;letter-spacing:4px}
.btn-small{font-size:9px;letter-spacing:3px}
.hero{top:126px;left:0;width:1200px;height:665px;background:radial-gradient(ellipse at 75% 30%,#1a5fb0 0%,#0d2d6b 40%,var(--navy-deep) 80%)}
.hero-photo{top:126px;left:583px;width:535px;height:665px;background:linear-gradient(180deg,rgba(40,80,150,.5),rgba(20,40,90,.8))}
.hero-title{left:61px;top:358px;font-size:45px;font-weight:500;line-height:53px;color:var(--white)}
.btn-outline{position:absolute;left:61px;top:499px;width:182px;height:48px;border:2px solid var(--blue);color:var(--blue);display:flex;align-items:center;justify-content:center;font-size:14px;font-weight:700;letter-spacing:4px}
.section-mark{width:64px;height:68px}
.section-title{font-size:28px;font-weight:700;letter-spacing:2px;color:var(--navy)}
.section-rule{height:2px;background:var(--blue);left:0}
.section-sub{font-size:16px;font-weight:500;letter-spacing:4px;line-height:20px;color:var(--blue)}
.about-copy{left:61px;top:1070px;width:520px;font-size:24px;line-height:32px;color:#111}
.about-block-light{left:704px;top:1000px;width:146px;height:236px;background:var(--blue)}
.about-block-dark{left:976px;top:1069px;width:152px;height:233px;background:#073d6d}
.about-photo{left:704px;top:877px;width:406px;height:641px;background:linear-gradient(180deg,#9fb4c8,#6f8aa5)}
.subscribe{top:1518px;left:0;width:1200px;height:432px;background:radial-gradient(ellipse at 70% 20%,#0f5592 0%,var(--navy) 55%,#0a3058 100%)}
.subscribe-title{top:1562px;left:0;width:1200px;text-align:center;font-size:26px;font-weight:500;letter-spacing:3px;color:var(--white)}
.label{font-size:13px;font-weight:700;letter-spacing:4px}
.subscribe .label,.label-light{color:var(--white)}
.field{background:var(--field);border:1px solid var(--field-line)}
.note{font-size:10px;font-weight:700;letter-spacing:1px;color:var(--white);text-align:center}
.service-card{width:211px;height:211px;border:3px solid #5fb7f0;box-shadow:0 2px 4px rgba(0,0,0,.2);display:flex;flex-direction:column;align-items:center;padding-top:28px}
.service-card svg{width:84px;height:76px}
.service-name{margin-top:14px;text-align:center;font-size:19px;font-weight:700;line-height:23px;color:var(--blue)}
.contact-line{right:69px;font-size:27px;font-weight:500;letter-spacing:5px;color:var(--blue);text-align:right}
.site-footer{top:3830px;left:0;width:1200px;height:227px;background:var(--footer)}
.site-footer .brand{position:absolute;left:62px;top:58px;color:var(--white)}
.social{position:absolute;top:50px;display:flex;align-items:center;gap:6px;color:var(--white);font-size:14px;font-weight:500}
.social-box{width:28px;height:28px;border:3px solid var(--white);border-radius:4px}
.footer-small{left:0;width:1200px;text-align:center;font-size:11px;letter-spacing:2px;color:var(--blue)}
</style>
</head>
<body>

<header class="abs site-header">
  <div class="brand"><span class="brand-mark"></span>KELVANE CONSULTING</div>
  <span class="nav" style="left:654px">HOME</span>
  <span class="nav" style="left:726px">ABOUT</span>
  <span class="nav" style="left:803px">SERVICES</span>
  <span class="nav" style="left:901px">CONTACT</span>
  <a class="btn btn-small" style="left:1003px;top:47px;width:126px;height:29px">GET STARTED</a>
</header>

<section class="abs hero"></section>
<div class="abs hero-photo" role="img" aria-label="Portrait of a smiling consultant in a navy suit with arms crossed, rising chart lines behind"></div>
<h1 class="abs hero-title">Helping your finance team<br>and increasing profit.</h1>
<a class="btn-outline">LEARN MORE</a>

<svg class="abs section-mark" style="left:58px;top:884px" viewBox="0 0 64 68"><rect x="0" y="0" width="32" height="32" fill="#00a8ef"/><rect x="18" y="10" width="44" height="34" fill="#0c3a66"/><rect x="6" y="34" width="30" height="32" fill="#18222f"/></svg>
<h2 class="abs section-title" style="left:105px;top:928px">ABOUT</h2>
<div class="abs section-rule" style="top:961px;width:214px"></div>
<p class="abs section-sub" style="left:103px;top:977px">TRANSFORMATIVE<br>FINANCE EXPERTISE</p>
<p class="abs about-copy">I am an experienced Finance professional who develops strategic financial plans, provides insightful analysis, and supports decision-making. With over 10 years of experience, I have successfully increased profitability for clients by $17M.</p>
<div class="abs about-block-light"></div>
<div class="abs about-block-dark"></div>
<div class="abs about-photo" role="img" aria-label="Consultant in a grey check blazer smiling at his phone"></div>
<a class="btn" style="left:828px;top:1381px;width:180px;height:43px">GET STARTED</a>

<section class="abs subscribe" role="img" aria-label="Deep blue background with faint chart lines"></section>
<h2 class="abs subscribe-title">SUBSCRIBE TO KELVANE</h2>
<span class="abs label label-light" style="left:347px;top:1632px">NAME</span>
<div class="abs field" style="left:343px;top:1652px;width:512px;height:46px"></div>
<span class="abs label label-light" style="left:347px;top:1718px">EMAIL</span>
<div class="abs field" style="left:343px;top:1740px;width:512px;height:45px"></div>
<p class="abs note" style="left:0;top:1803px;width:1200px">YOU CAN UNSUBSCRIBE AT ANY TIME. WE DO NOT SPAM.</p>
<a class="btn" style="left:542px;top:1855px;width:115px;height:45px">SUBMIT</a>

<svg class="abs section-mark" style="left:58px;top:2029px" viewBox="0 0 64 68"><rect x="0" y="0" width="32" height="32" fill="#00a8ef"/><rect x="18" y="10" width="44" height="34" fill="#0c3a66"/><rect x="6" y="34" width="30" height="32" fill="#18222f"/></svg>
<h2 class="abs section-title" style="left:105px;top:2073px">SERVICES</h2>
<div class="abs section-rule" style="top:2106px;width:258px"></div>
<p class="abs section-sub" style="left:103px;top:2121px">EMPOWER YOUR<br>FINANCIAL FUTURE</p>

<div class="abs service-card" style="left:156px;top:2238px">
  <svg viewBox="0 0 84 76" fill="none" stroke="#0c3a66" stroke-width="3"><rect x="10" y="40" width="14" height="32"/><rect x="32" y="28" width="14" height="44"/><rect x="54" y="8" width="14" height="64"/><circle cx="18" cy="20" r="10"/><path d="M18 13v14M14 17h7M14 23h7"/><path d="M4 72h76"/></svg>
  <div class="service-name">FINANCIAL<br>MODELS AND<br>PROJECTS</div>
</div>
<div class="abs service-card" style="left:495px;top:2238px">
  <svg viewBox="0 0 84 76" fill="none" stroke="#0c3a66" stroke-width="3"><rect x="22" y="10" width="40" height="64" rx="6"/><path d="M22 18h40"/><circle cx="36" cy="36" r="8"/><circle cx="50" cy="48" r="8"/><circle cx="36" cy="60" r="8"/></svg>
  <div class="service-name">BUDGETING<br>PROCESS</div>
</div>
<div class="abs service-card" style="left:833px;top:2238px">
  <svg viewBox="0 0 84 76" fill="none" stroke="#0c3a66" stroke-width="3"><circle cx="16" cy="30" r="7"/><circle cx="42" cy="30" r="7"/><circle cx="68" cy="30" r="7"/><path d="M6 58v-10h20v10M32 58v-10h20v10M58 58v-10h20v10"/><path d="M2 60h80"/></svg>
  <div class="service-name">TEMPORARY<br>STAFFING</div>
</div>
<div class="abs service-card" style="left:326px;top:2507px">
  <svg viewBox="0 0 84 76" fill="none" stroke="#0c3a66" stroke-width="3"><path d="M18 34a24 24 0 0 1 40-18"/><path d="M52 10l6 6-8 3"/><path d="M66 42a24 24 0 0 1-40 18"/><path d="M32 66l-6-6 8-3"/><rect x="32" y="26" width="20" height="24"/><path d="M36 34h12M36 40h12"/></svg>
  <div class="service-name">DATA<br>CLEANSING</div>
</div>
<div class="abs service-card" style="left:661px;top:2507px">
  <svg viewBox="0 0 84 76" fill="none" stroke="#0c3a66" stroke-width="3"><path d="M30 18L42 6l12 12"/><rect x="6" y="18" width="64" height="44"/><path d="M14 52l12-14 10 8 14-16 8 6"/><circle cx="64" cy="58" r="12" fill="#fff"/><path d="M64 50v8l5 4"/></svg>
  <div class="service-name">PROCESS<br>IMPROVEMENT</div>
</div>
<a class="btn" style="left:510px;top:2813px;width:180px;height:46px">GET STARTED</a>

<svg class="abs section-mark" style="left:58px;top:3025px" viewBox="0 0 64 68"><rect x="0" y="0" width="32" height="32" fill="#00a8ef"/><rect x="18" y="10" width="44" height="34" fill="#0c3a66"/><rect x="6" y="34" width="30" height="32" fill="#18222f"/></svg>
<h2 class="abs section-title" style="left:105px;top:3069px">CONTACT</h2>
<div class="abs section-rule" style="top:3103px;width:246px"></div>
<p class="abs section-sub" style="left:103px;top:3120px">ACHIEVING PROSPERITY<br>TOGETHER</p>

<span class="abs label" style="left:64px;top:3236px">NAME</span>
<div class="abs field" style="left:60px;top:3259px;width:439px;height:45px"></div>
<span class="abs label" style="left:64px;top:3323px">EMAIL</span>
<div class="abs field" style="left:60px;top:3345px;width:439px;height:46px"></div>
<span class="abs label" style="left:64px;top:3406px">PHONE</span>
<div class="abs field" style="left:60px;top:3429px;width:439px;height:44px"></div>
<span class="abs label" style="left:64px;top:3493px">MESSAGE</span>
<div class="abs field" style="left:60px;top:3517px;width:439px;height:120px"></div>
<a class="btn" style="left:60px;top:3662px;width:116px;height:44px">SEND</a>

<p class="abs contact-line" style="top:3366px">INFO@KELVANE.COM</p>
<p class="abs contact-line" style="top:3405px">+1 (555) 014-276</p>

<footer class="abs site-footer">
  <div class="brand"><span class="brand-mark"></span>KELVANE CONSULTING</div>
  <div class="social" style="left:918px"><span class="social-box"></span>Linkora</div>
  <svg class="abs" style="left:1018px;top:50px" width="40" height="30" viewBox="0 0 40 30" fill="none" stroke="#fff" stroke-width="3"><rect x="2" y="2" width="36" height="26" rx="2"/><path d="M2 4l18 13L38 4"/></svg>
  <div class="social" style="left:1070px;top:88px;font-size:12px"></div>
  <div class="social" style="left:1076px"><span class="social-box" style="border-radius:50%"></span></div>
  <p class="abs footer-small" style="top:150px">PRIVACY POLICY</p>
  <p class="abs footer-small" style="top:174px">©2023 - ALL RIGHTS RESERVED</p>
</footer>

</body>
</html>
```